Business Card and Stationary design for new logo
Bright Harbour Makeovers
Professional
Tessa Whitlock & Lewis Whitlock
Director
42 Quenby Crescent
Carrow Vale NSW 2999
brightharbourmakeovers@fernpost.example
ABN:284 907 362
Color combinations need to remain within company palette of ORANGE, TAN, BLACK AND WHITE. Would prefer ORANGE as main background color for business card design and therefore will need to invert actual logo colors to be able to see all of the design. Would prefer BLACK as the main background color for stationary design as currently have templates where the logo would need to be inserted however would be interested in seeing other designs to make final decision.

```html
<!DOCTYPE html>
<html lang="en">
<head>
<meta charset="utf-8">
<title>Bright Harbour Makeovers – Stationery</title>
<link rel="stylesheet" href="https://fonts.googleapis.com/css2?family=Open+Sans:wght@400;700&display=swap">
<style>
  :root{
    --backdrop:#5b3322;
    --paper:#ffffff;
    --orange:#e8761e;
    --orange-deep:#b8480c;
    --black:#1c1c1c;
    --grey:#8a8a8a;
    --faint:#ececec;
  }
  html,body{margin:0;padding:0;overflow:hidden;}
  body{width:1200px;height:553px;background:var(--backdrop);position:relative;font-family:"Open Sans",Arial,sans-serif;}
  .sheet{position:absolute;background:var(--paper);overflow:hidden;box-shadow:0 3px 10px rgba(0,0,0,.35);}
  .wave{position:absolute;left:0;width:100%;display:block;}
  .brand{position:absolute;display:flex;align-items:center;gap:4px;white-space:nowrap;}
  .brand .dot{border-radius:50%;background:var(--orange);flex:none;}
  .brand .name{font-weight:700;color:var(--black);line-height:1;}
  .brand.on-dark .name{color:var(--paper);}
  .brand.on-dark .dot{background:var(--paper);}
  .mark-faint{position:absolute;border-radius:50%;border:10px solid var(--faint);box-sizing:border-box;display:flex;align-items:center;justify-content:center;}
  .mark-faint span{font-weight:700;color:var(--faint);text-align:center;line-height:1.1;}
  .contact{position:absolute;text-align:right;font-size:3.6px;line-height:1.45;color:var(--grey);white-space:nowrap;}
  .contact.on-orange{color:var(--paper);}
  .contact.left{text-align:left;}

  .letterhead-a{left:43px;top:62px;width:293px;height:394px;}
  .letterhead-back{left:523px;top:34px;width:298px;height:422px;z-index:1;}
  .letterhead-b{left:355px;top:96px;width:298px;height:427px;z-index:2;}
  .card-front{left:835px;top:60px;width:156px;height:84px;}
  .card-back{left:1008px;top:60px;width:168px;height:84px;background:linear-gradient(90deg,var(--orange-deep),var(--orange) 45%,#f29a4a 60%,var(--orange-deep));}
  .envelope{left:833px;top:175px;width:343px;height:130px;}
  .envelope .flap{position:absolute;left:0;top:0;width:100%;height:52px;background:linear-gradient(90deg,#2a1408,var(--orange-deep) 30%,var(--orange) 50%,var(--orange-deep) 70%,#2a1408);}
  .slip{left:833px;top:329px;width:343px;height:165px;}
</style>
</head>
<body>

<div class="sheet letterhead-a">
  <svg class="wave" style="top:0;height:40px" viewBox="0 0 100 14" preserveAspectRatio="none">
    <path d="M0 2 C30 12 60 12 100 6 L100 0 L0 0Z" fill="var(--orange)"/>
    <path d="M0 4 C30 13 60 13 100 8" fill="none" stroke="var(--grey)" stroke-width=".3"/>
  </svg>
  <div class="brand" style="left:8px;top:12px"><span class="dot" style="width:12px;height:12px"></span><span class="name" style="font-size:8px">Bright Harbour Makeovers</span></div>
  <div class="contact on-orange" style="right:8px;top:4px">42 Quenby Crescent<br>Carrow Vale NSW 2999<br>brightharbourmakeovers@fernpost.example<br>ABN: 284 907 362</div>
  <div class="mark-faint" style="left:65px;top:82px;width:180px;height:180px"><span style="font-size:18px">Bright Harbour<br>Makeovers</span></div>
</div>

<div class="sheet letterhead-back">
  <div class="brand" style="left:54px;top:12px"><span class="dot" style="width:14px;height:14px"></span><span class="name" style="font-size:9px">Bright Harbour Makeovers</span></div>
  <div class="contact" style="right:10px;top:10px">42 Quenby Crescent<br>Carrow Vale NSW 2999<br>brightharbourmakeovers@fernpost.example<br>ABN: 284 907 362</div>
  <svg class="wave" style="bottom:0;height:34px" viewBox="0 0 100 14" preserveAspectRatio="none">
    <path d="M0 6 C30 0 65 12 100 4 L100 14 L0 14Z" fill="var(--orange)"/>
    <path d="M0 8 C30 2 65 14 100 6" fill="none" stroke="var(--paper)" stroke-width=".8"/>
  </svg>
</div>

<div class="sheet letterhead-b">
  <div class="brand" style="left:50%;transform:translateX(-50%);top:16px"><span class="dot" style="width:14px;height:14px"></span><span class="name" style="font-size:9px">Bright Harbour Makeovers</span></div>
  <div class="mark-faint" style="left:65px;top:96px;width:170px;height:170px"><span style="font-size:17px">Bright Harbour<br>Makeovers</span></div>
  <svg class="wave" style="bottom:0;height:48px" viewBox="0 0 100 14" preserveAspectRatio="none">
    <path d="M0 6 C30 0 65 12 100 4 L100 14 L0 14Z" fill="var(--orange)"/>
    <path d="M0 8 C30 2 65 14 100 6" fill="none" stroke="var(--paper)" stroke-width=".8"/>
    <path d="M0 5 C30 -1 65 11 100 3" fill="none" stroke="var(--black)" stroke-width=".3"/>
  </svg>
  <div class="brand" style="left:50%;transform:translateX(-50%);bottom:12px;background:var(--paper);padding:2px 4px"><span class="dot" style="width:8px;height:8px"></span><span class="name" style="font-size:5px">Bright Harbour Makeovers</span></div>
</div>

<div class="sheet card-front">
  <div class="brand" style="left:6px;top:6px"><span class="dot" style="width:9px;height:9px"></span><span class="name" style="font-size:5px">Bright Harbour Makeovers</span></div>
  <div class="contact left" style="left:6px;top:30px;color:var(--orange-deep)"><b>Tessa Whitlock</b><br>Director<br><b>Lewis Whitlock</b><br>Director</div>
  <div class="contact" style="right:6px;top:30px">42 Quenby Crescent<br>Carrow Vale NSW 2999<br>ABN: 284 907 362</div>
  <svg class="wave" style="bottom:0;height:18px" viewBox="0 0 100 14" preserveAspectRatio="none">
    <path d="M0 6 C30 0 65 12 100 4 L100 14 L0 14Z" fill="var(--orange)"/>
  </svg>
</div>

<div class="sheet card-back">
  <div class="mark-faint" style="left:49px;top:7px;width:70px;height:70px;border-color:rgba(255,255,255,.3);border-width:5px"><span style="font-size:7px;color:rgba(255,255,255,.35)">Bright Harbour<br>Makeovers</span></div>
</div>

<div class="sheet envelope">
  <div class="flap"></div>
  <div class="brand on-dark" style="left:50%;transform:translateX(-50%);top:20px"><span class="dot" style="width:10px;height:10px"></span><span class="name" style="font-size:6px">Bright Harbour Makeovers</span></div>
</div>

<div class="sheet slip">
  <div class="brand" style="left:8px;top:14px"><span class="dot" style="width:12px;height:12px"></span><span class="name" style="font-size:7px">Bright Harbour Makeovers</span></div>
  <div class="mark-faint" style="right:18px;top:20px;width:90px;height:90px;border-width:6px"><span style="font-size:8px">Bright Harbour<br>Makeovers</span></div>
  <svg class="wave" style="bottom:0;height:26px" viewBox="0 0 100 14" preserveAspectRatio="none">
    <path d="M0 6 C30 0 65 12 100 4 L100 14 L0 14Z" fill="var(--orange)"/>
  </svg>
</div>

</body>
</html>
```